Design some Business Cards for Kestrel Works

I need a design for business cards. I have an existing logo.

I am a sole trader (work for myself) and I provide computer and IT technology support services to small businesses in Australia. I advise business owners on how to best use and manage their IT systems and computers and I provide onsite computer troubleshooting services.
The style should reflect the professional nature of my work.
I would likely favour a simpler and clean design.

The artwork needs to be:
Single sided (just the front of the card)
89mm x 54mm in size.
Full colour.
To be printed on white stock (paper)

Details that need to be included on the business cards are:
Logo
Name Milo Brennard
Email address milo@kestrelworks-mail.com.au
Phone number 0423 587 219

The exact details will be supplied at the end of the contest for the final artwork.
Final artwork would need to be print ready – I can provide examples of what they need to look like.

```html
<!DOCTYPE html>
<html lang="en">
<head>
<meta charset="utf-8">
<title>Kestrel Works – Business Card</title>
<link href="https://fonts.googleapis.com/css2?family=Oswald:wght@400;600&family=Roboto:wght@400;500&display=swap" rel="stylesheet">
<style>
  :root {
    --page-bg: #e8eaee;
    --card-white: #ffffff;
    --card-shade: #f1f2f5;
    --accent-blue: #3e9fe0;
    --brand-blue: #2f6fb5;
    --ink-dark: #2b2e33;
    --ink-mid: #4a4f57;
    --soft-grey: #e3e4e8;
  }
  html, body {
    margin: 0;
    padding: 0;
    width: 1200px;
    height: 2577px;
    overflow: hidden;
    background: var(--page-bg);
  }
  .card {
    position: absolute;
    left: 100px;
    top: 985px;
    width: 1000px;
    height: 607px;
    background: linear-gradient(180deg, var(--card-white) 0%, var(--card-shade) 100%);
    box-shadow: 0 14px 40px rgba(40, 50, 70, 0.18);
    overflow: hidden;
  }
  .corner-tab {
    position: absolute;
    right: 0;
    top: 70px;
    width: 60px;
    height: 56px;
    background: var(--soft-grey);
  }
  .brand {
    position: absolute;
    left: 470px;
    top: 80px;
    display: flex;
    align-items: center;
    gap: 24px;
  }
  .brand-dot {
    width: 76px;
    height: 76px;
    border-radius: 50%;
    background: var(--brand-blue);
    flex: none;
  }
  .brand-name {
    font-family: "Oswald", sans-serif;
    font-weight: 400;
    font-size: 62px;
    line-height: 1;
    color: var(--brand-blue);
    margin: 0;
    white-space: nowrap;
  }
  .brand-tagline {
    font-family: "Roboto", sans-serif;
    font-size: 18px;
    letter-spacing: 0.3px;
    color: var(--ink-mid);
    margin: 6px 0 0 2px;
    white-space: nowrap;
  }
  .name-band {
    position: absolute;
    left: 0;
    top: 328px;
    width: 1000px;
    height: 58px;
    display: flex;
    align-items: center;
  }
  .band-stub {
    width: 16px;
    height: 58px;
    background: var(--accent-blue);
    flex: none;
  }
  .holder-name {
    font-family: "Oswald", sans-serif;
    font-weight: 600;
    font-size: 54px;
    letter-spacing: 0.5px;
    text-transform: uppercase;
    color: var(--ink-dark);
    margin: 0 22px;
    white-space: nowrap;
  }
  .band-bar {
    flex: 1;
    height: 38px;
    background: var(--accent-blue);
  }
  .contacts {
    position: absolute;
    left: 42px;
    top: 420px;
    list-style: none;
    margin: 0;
    padding: 0;
    font-family: "Roboto", sans-serif;
    font-size: 26px;
    color: var(--ink-dark);
  }
  .contacts li {
    display: flex;
    align-items: center;
    gap: 14px;
    height: 52px;
  }
  .contacts svg {
    width: 24px;
    height: 24px;
    flex: none;
  }
</style>
</head>
<body>
  <div class="card">
    <div class="corner-tab"></div>

    <div class="brand">
      <div class="brand-dot"></div>
      <div>
        <p class="brand-name">Kestrel Works</p>
        <p class="brand-tagline">Onsite IT Help for Small Business</p>
      </div>
    </div>

    <div class="name-band">
      <div class="band-stub"></div>
      <h1 class="holder-name">Milo Brennard</h1>
      <div class="band-bar"></div>
    </div>

    <ul class="contacts">
      <li>
        <svg viewBox="0 0 24 24" aria-hidden="true">
          <circle cx="12" cy="12" r="11" fill="var(--ink-dark)"/>
          <ellipse cx="12" cy="12" rx="4.5" ry="10" fill="none" stroke="#fff" stroke-width="1.5"/>
          <line x1="2" y1="12" x2="22" y2="12" stroke="#fff" stroke-width="1.5"/>
        </svg>
        www.kestrelworks.net.au
      </li>
      <li>
        <svg viewBox="0 0 24 24" aria-hidden="true">
          <rect x="1" y="1" width="22" height="22" rx="5" fill="var(--ink-dark)"/>
          <path d="M8 5.5l2.2 3-1.4 1.6c.8 1.8 2.3 3.3 4.1 4.1l1.6-1.4 3 2.2-1.3 2.5c-5.5-.5-10-5-10.5-10.5z" fill="#fff"/>
        </svg>
        Tel: 0423 587 219
      </li>
      <li>
        <svg viewBox="0 0 24 24" aria-hidden="true">
          <rect x="1" y="4" width="22" height="16" rx="1.5" fill="var(--ink-dark)"/>
          <path d="M2 5.5l10 7.5 10-7.5" fill="none" stroke="#fff" stroke-width="1.6"/>
        </svg>
        milo@kestrelworks-mail.com.au
      </li>
    </ul>
  </div>
</body>
</html>
```